Reaching the Right Campus Might Be Simpler Than Expected! Nine Moves Toward Stronger Report Cards...

I need a cover/front/spine/back for an e-book and a hard cover book that I am publishing on Zembrix. I have written a book with an eight step process on how to help parents coach their kids to getting grades up and accepted into good colleges. In the book, I am highlighting current day struggles teens and young adults are having with mental health due to the impact of social media. I am helping them understand the impact mental health and social media has had on school stress. I outline a process in my book that my reader can implement herself with her child, or hire me as her coach.

Target Market(s)

Women ages 35 to 55 with teens in high school and college

Industry/Entity Type

Life Coaching

Font styles to use
Serif

Colors

Designer to choose colors to be used in the design.

Requirements
Must have
• Title, name, (credentials/PhD) and simple image on cover. Font and
• point size that you can read in a teeny, tiny thumbnail. Readability is number one goal. Text on thumbnail must be readable. I have been made aware that subtitles are hard to get on E-books.
Nice to have
• Something that immediately lets the reader know what my book is about
Should not have
• No italics or swirly curly font.

```html
<!DOCTYPE html>
<html lang="en">
<head>
<meta charset="utf-8">
<title>Reaching the Right Campus Might Be Simpler Than Expected! — Front Cover</title>
<link rel="stylesheet" href="https://fonts.googleapis.com/css2?family=Libre+Baskerville:wght@400;700&family=Open+Sans:wght@400&display=swap">
<style>
  :root {
    --stage: #e9e6e1;
    --paper: #ffffff;
    --navy: #15396b;
    --orange: #f06e2c;
    --ink: #141414;
    --photo-light: #f3f5f6;
    --photo-teal: #3f8f86;
    --photo-deep: #1f5a5c;
  }
  * { box-sizing: border-box; margin: 0; padding: 0; }
  html, body {
    width: 1200px;
    height: 1070px;
    overflow: hidden;
    background: var(--stage);
  }
  .canvas {
    position: relative;
    width: 1200px;
    height: 1070px;
    display: flex;
    align-items: center;
    justify-content: center;
  }
  .front-cover {
    position: relative;
    width: 640px;
    height: 970px;
    background: var(--paper);
    box-shadow: 0 10px 30px rgba(0,0,0,0.18);
    overflow: hidden;
  }
  .cover-title {
    position: absolute;
    left: 52px;
    top: 48px;
    width: 560px;
    font-family: "Libre Baskerville", "Palatino Linotype", serif;
    font-weight: 700;
    font-size: 50px;
    line-height: 1.3;
    letter-spacing: 0.5px;
    color: var(--navy);
    text-transform: uppercase;
  }
  .subtitle-band {
    position: absolute;
    left: 32px;
    right: 14px;
    top: 418px;
    height: 130px;
    background: var(--orange);
    padding: 16px 30px 0 40px;
    font-family: "Open Sans", "Segoe UI", sans-serif;
    font-weight: 400;
    font-size: 27px;
    line-height: 1.2;
    color: var(--paper);
  }
  .cover-photo {
    position: absolute;
    left: 60px;
    right: 14px;
    top: 568px;
    bottom: 0;
    background:
      radial-gradient(ellipse 55% 60% at 52% 58%, var(--photo-teal) 0%, var(--photo-deep) 45%, rgba(31,90,92,0) 75%),
      linear-gradient(180deg, var(--paper) 0%, var(--photo-light) 100%);
  }
  .author-name {
    position: absolute;
    left: 0;
    right: 0;
    bottom: 48px;
    text-align: center;
    padding-left: 80px;
    font-family: "Libre Baskerville", "Palatino Linotype", serif;
    font-weight: 400;
    font-size: 44px;
    letter-spacing: 1px;
    color: var(--ink);
    text-transform: uppercase;
  }
</style>
</head>
<body>
  <main class="canvas">
    <article class="front-cover">
      <h1 class="cover-title">Reaching the Right Campus Might Be Simpler Than Expected!</h1>
      <p class="subtitle-band">Nine move process on how to help parents coach their kids toward stronger report cards and the right campus</p>
      <div class="cover-photo" role="img" aria-label="Photo of a thoughtful teenage student in a green plaid shirt with headphones, leaning on a desk beside a stack of notebooks and a coffee cup"></div>
      <p class="author-name">Author Name</p>
    </article>
  </main>
</body>
</html>
```